Eye catching while remaining subtle, stylish and professional

Plover Works are a Heatpump and Air Conditioning Company. I would like stationary that would be suitable to use for letters, quoting invoicing. The final design should communicate a trade/service type industry that is clean and professional

I would like the designer to also offer a Business card option as well.

Details should include company logo as attached. Company details. Name, Address, Phone, Email and Website. You can use generic details until a final design is chosen

Target Market(s)

Trade/Service Industry

Industry/Entity Type

Air Conditioning

Requirements
Must have
• LOGO, Company contact details
Nice to have
• Watermark

```html
<!DOCTYPE html>
<html lang="en">
<head>
<meta charset="utf-8">
<title>Plover Works – Business Card</title>
<link rel="stylesheet" href="https://fonts.googleapis.com/css2?family=Mulish:wght@400;700&display=swap">
<style>
  :root {
    --page-bg: #e9e6e2;
    --card-top: #f4f6f8;
    --card-bottom: #e6eaee;
    --card-edge: #cfd5da;
    --brand-blue: #2a8ac0;
    --text-grey: #5a5f63;
    --rule: #c8cfd5;
    --band: #dde3e8;
  }
  * { box-sizing: border-box; margin: 0; padding: 0; }
  html, body { width: 1200px; height: 970px; overflow: hidden; }
  body {
    background: var(--page-bg);
    font-family: "Mulish", "Century Gothic", sans-serif;
    position: relative;
  }
  .business-card {
    position: absolute;
    left: 100px; top: 207px;
    width: 1000px; height: 556px;
    background: linear-gradient(160deg, var(--card-top), var(--card-bottom));
    border: 1px solid var(--card-edge);
    box-shadow: 0 10px 30px rgba(0,0,0,0.12);
    overflow: hidden;
  }
  .brand {
    position: absolute;
    left: 50px; top: 0; width: 418px; height: 500px;
    display: flex; align-items: center; justify-content: center; gap: 12px;
    white-space: nowrap;
  }
  .brand-dot {
    flex: none;
    width: 26px; height: 26px; border-radius: 50%;
    background: var(--brand-blue);
  }
  .brand-name {
    color: var(--brand-blue);
    font-weight: 700;
    font-size: 40px;
    letter-spacing: 1px;
    text-transform: uppercase;
  }
  .divider {
    position: absolute;
    left: 518px; top: 60px;
    width: 1px; height: 380px;
    background: var(--rule);
  }
  .details {
    position: absolute;
    left: 606px; top: 118px;
    color: var(--text-grey);
  }
  .person-name {
    color: var(--brand-blue);
    font-weight: 700;
    font-size: 27px;
    letter-spacing: 1px;
  }
  .person-role { font-size: 22px; margin-top: 2px; }
  .contact-list { list-style: none; margin-top: 30px; }
  .contact-item {
    display: flex; align-items: center; gap: 10px;
    font-size: 22px; line-height: 33px;
  }
  .contact-icon {
    width: 22px; height: 22px; border-radius: 3px;
    background: var(--brand-blue);
    display: flex; align-items: center; justify-content: center;
  }
  .address { font-size: 22px; line-height: 33px; margin-top: 22px; }
  .pattern-band {
    position: absolute;
    left: 0; bottom: 0; width: 100%; height: 56px;
    background: linear-gradient(90deg, var(--band), #e8ecef, var(--band));
  }
</style>
</head>
<body>
  <article class="business-card">
    <div class="brand">
      <span class="brand-dot"></span>
      <span class="brand-name">Plover Works</span>
    </div>
    <div class="divider"></div>
    <section class="details">
      <h1 class="person-name">JORDAN MERCER</h1>
      <p class="person-role">General Manager</p>
      <ul class="contact-list">
        <li class="contact-item">
          <span class="contact-icon">
            <svg width="14" height="14" viewBox="0 0 14 14"><path d="M3 1 L5 1 L6 4 L4.5 5 Q6 8 9 9.5 L10 8 L13 9 L13 11 Q13 13 11 13 Q2 12 1 3 Q1 1 3 1 Z" fill="#fff"/></svg>
          </span>
          009 71 43 00 26
        </li>
        <li class="contact-item">
          <span class="contact-icon">
            <svg width="14" height="12" viewBox="0 0 14 12"><rect x="1" y="2" width="12" height="8" fill="none" stroke="#fff" stroke-width="1.4"/><path d="M1 2 L7 7 L13 2" fill="none" stroke="#fff" stroke-width="1.4"/></svg>
          </span>
          info@ploverworks.com
        </li>
        <li class="contact-item">
          <span class="contact-icon">
            <svg width="14" height="14" viewBox="0 0 14 14"><circle cx="7" cy="7" r="5.5" fill="none" stroke="#fff" stroke-width="1.3"/><ellipse cx="7" cy="7" rx="2.4" ry="5.5" fill="none" stroke="#fff" stroke-width="1.1"/><path d="M1.5 7 H12.5" stroke="#fff" stroke-width="1.1"/></svg>
          </span>
          www.ploverworks.com
        </li>
      </ul>
      <p class="address">5/18 Harlow Street<br>Denbury, VIC 3172</p>
    </section>
    <div class="pattern-band" role="img" aria-label="Faint band of repeating decorative snowflake-branch pattern"></div>
  </article>
</body>
</html>
```